One of Australia's fastest growing Financial Company looking for an updated business card design!

Meridale Holdings Australia is looking for an updated design for our business cards. We would like to keep up our professional appearances and have get new exciting design that fits our company.

The Meridale aim is to facilitate and assist clients in every financial requirement that may arise in financial areas.

We would to see the design to use colour blue and we like the clouds in the background. We have attached two designs we have use before but we need something with more professional and easy to read design.

We would like the website in the back of the card; the employees name more central and stands out; only a postal address; a list of all our locations along the bottom (Sydney, Melbourne, Brisbane, Singapore)

Looking forward to seeing the designs come in!

Target Market(s)

Other Industry Professionals
Middle Class Families

Industry/Entity Type

Finance

Contact Information for Business Card

Name; Company Role; Office Number; Mobile Number; Email Address; Website; Postal Address; Locations

Font styles to use
Serif
Sans Serif

Colors
0492cd
33a6d7
85cae6
85acd3
3176b5
0455a3
cee9f5
d5e2ee

Requirements
Must have
• Name; Company Role; Office Number; Mobile Number; Email Address; Website; Postal Address; Locations
Nice to have
• The colour blue, clouds on the background

```html
<!DOCTYPE html>
<html lang="en">
<head>
<meta charset="utf-8">
<title>Meridale Holdings Australia — Business Card</title>
<link rel="stylesheet" href="https://fonts.googleapis.com/css2?family=Arimo:wght@400;700&display=swap">
<style>
  :root{
    --stage:#2a2a2b;
    --sky-deep:#3176b5;
    --sky-mid:#85acd3;
    --sky-light:#cee9f5;
    --band-dark:#0492cd;
    --band-light:#85cae6;
    --paper:#f4f6f8;
    --ink:#1c1c1c;
    --accent-red:#d6262f;
    --brand-blue:#0455a3;
    --contact-blue:#0455a3;
    --white:#ffffff;
  }
  *{box-sizing:border-box;margin:0;padding:0}
  html,body{width:1200px;height:997px;overflow:hidden;background:var(--stage);font-family:"Arimo",Arial,sans-serif}
  .stage{position:relative;width:1200px;height:997px}

  .card{position:absolute;width:600px;height:343px;overflow:hidden;box-shadow:0 18px 40px rgba(0,0,0,.55)}
  .card svg.card-art{position:absolute;inset:0;width:100%;height:100%}

  /* back of card */
  .card--back{left:50px;top:90px}
  .card--back .brand{position:absolute;right:40px;top:128px;display:flex;align-items:center;gap:12px}
  .card--back .brand-name{font-size:50px;font-weight:700;color:var(--white);letter-spacing:.5px}
  .card--back .brand-dot{width:26px;height:26px;border-radius:50%;background:var(--accent-red)}
  .card--back .locations{position:absolute;right:40px;top:198px;font-size:17px;font-weight:700;color:var(--white);letter-spacing:.3px}

  /* front of card */
  .card--front{left:550px;top:470px}
  .card--front .brand{position:absolute;left:46px;top:92px;display:flex;align-items:center;gap:12px}
  .card--front .brand-dot{width:28px;height:28px;border-radius:50%;background:var(--accent-red)}
  .card--front .brand-name{font-size:54px;font-weight:700;color:var(--brand-blue);letter-spacing:.5px}

  .person{position:absolute;right:30px;top:160px;text-align:right}
  .person-name{font-size:21px;font-weight:700;color:var(--accent-red)}
  .person-role{font-size:15px;color:var(--ink);margin-top:2px}
  .contact-list{list-style:none;margin-top:8px}
  .contact-list li{display:flex;justify-content:flex-end;align-items:center;gap:8px;font-size:11.5px;font-weight:700;color:var(--contact-blue);line-height:18px}
  .contact-list svg{width:11px;height:11px;fill:var(--ink)}
  .postal{position:absolute;right:30px;bottom:24px;font-size:12.5px;font-weight:700;color:var(--contact-blue)}
</style>
</head>
<body>
<main class="stage">

  <section class="card card--back" aria-label="Back of business card">
    <svg class="card-art" viewBox="0 0 600 343" role="img" aria-label="Photograph of bright sun rays breaking through white clouds in a blue sky">
      <defs>
        <radialGradient id="skyBack" cx="0.32" cy="0.5" r="0.85">
          <stop offset="0" stop-color="#ffffff"/>
          <stop offset="0.18" stop-color="#cee9f5"/>
          <stop offset="0.55" stop-color="#85acd3"/>
          <stop offset="1" stop-color="#3176b5"/>
        </radialGradient>
      </defs>
      <rect width="600" height="343" fill="url(#skyBack)"/>
    </svg>
    <div class="brand"><span class="brand-dot"></span><span class="brand-name">Meridale</span></div>
    <p class="locations">Sydney, Melbourne, Brisbane, Singapore</p>
  </section>

  <section class="card card--front" aria-label="Front of business card">
    <svg class="card-art" viewBox="0 0 600 343">
      <defs>
        <radialGradient id="skyFront" cx="0.33" cy="0.4" r="0.8">
          <stop offset="0" stop-color="#ffffff"/>
          <stop offset="0.2" stop-color="#cee9f5"/>
          <stop offset="0.6" stop-color="#85acd3"/>
          <stop offset="1" stop-color="#3176b5"/>
        </radialGradient>
      </defs>
      <rect class="paper" width="600" height="343" fill="#f4f6f8"/>
      <path class="wave-band-dark" fill="#0492cd" d="M0,0 H600 V125 C480,130 390,180 300,220 C200,265 100,282 0,280 Z"/>
      <path class="wave-band-light" fill="#85cae6" d="M0,0 H600 V113 C480,118 390,168 300,208 C200,253 100,270 0,268 Z"/>
      <path class="sky" fill="url(#skyFront)" d="M0,0 H600 V105 C480,110 390,160 300,200 C200,245 100,262 0,260 Z" role="img" aria-label="Photograph of sun rays through clouds in a blue sky"/>
    </svg>

    <div class="brand"><span class="brand-dot"></span><span class="brand-name">Meridale</span></div>

    <div class="person">
      <p class="person-name">Elena Marsh</p>
      <p class="person-role">Managing Partner</p>
      <ul class="contact-list">
        <li>+1 (203) 555-0142 <svg viewBox="0 0 12 12" aria-label="Office"><path d="M1 4c2-3 8-3 10 0l-2 1-1-1H4L3 5z M3 6h6l1 5H2z"/></svg></li>
        <li>+1 (914) 555-0178 <svg viewBox="0 0 12 12" aria-label="Mobile"><path d="M3 0h6v12H3z M4 1v9h4V1z"/></svg></li>
        <li>care@meridale.com <svg viewBox="0 0 12 12" aria-label="Email"><path d="M0 2h12v8H0z M1 3l5 4 5-4z" fill-rule="evenodd"/></svg></li>
        <li>www.meridale.com <svg viewBox="0 0 12 12" aria-label="Website"><circle cx="6" cy="6" r="5.5"/></svg></li>
      </ul>
    </div>

    <p class="postal">42 Birchwood Lane, 2nd Floor, Fairview, CT 06410</p>
  </section>

</main>
</body>
</html>
```